Solar appointment reminder card

We are looking for a new design for our appointment reminder card since we have changed our logo. The card should have the new logo along with space for the employee to hand write the customers appointment date, time, the employees name and phone number.
I've uploaded what our old basic appointment card looked like and our new logo.

The cards should be in a standard business card size and could be horizontal or vertical.

```html
<!DOCTYPE html>
<html lang="en">
<head>
<meta charset="utf-8">
<title>Lumera Solar – Appointment Card</title>
<link rel="stylesheet" href="https://fonts.googleapis.com/css2?family=Montserrat:wght@400;600;800&family=Roboto:wght@400&display=swap">
<style>
  :root {
    --page-bg: #e7ecef;
    --front-top: #86421f;
    --front-bottom: #f28f47;
    --brand-orange: #ee8a2c;
    --heading-yellow: #f5b81c;
    --label-grey: #3c3c3c;
    --rule-grey: #a9a9a9;
    --band-orange: #e37b17;
    --band-grey-light: #8a8a8a;
    --band-grey-dark: #4a4a4a;
    --white: #ffffff;
  }
  * { box-sizing: border-box; margin: 0; padding: 0; }
  html, body {
    width: 768px; height: 1200px; overflow: hidden;
    background: var(--page-bg);
    font-family: "Montserrat", sans-serif;
  }
  .sheet {
    position: relative; width: 768px; height: 1200px;
    display: flex; flex-direction: column; align-items: center; justify-content: center; gap: 40px;
  }
  .card {
    position: relative; width: 640px; height: 368px; overflow: hidden;
    box-shadow: 0 4px 12px rgba(0,0,0,0.22);
  }

  /* Front */
  .card--front {
    background: linear-gradient(180deg, var(--front-top) 0%, var(--front-bottom) 100%);
  }
  .landmark-area {
    position: absolute; right: 28px; top: 10px; width: 70px; height: 250px;
    border-radius: 30px 30px 4px 4px;
    background: linear-gradient(180deg, rgba(255,255,255,0.05), rgba(255,255,255,0.02));
  }
  .wordmark {
    display: flex; align-items: center; gap: 12px;
    font-weight: 800; letter-spacing: 1px; text-transform: uppercase; white-space: nowrap;
  }
  .wordmark__dot { flex: none; border-radius: 50%; }
  .card--front .wordmark {
    position: absolute; left: 0; right: 0; top: 150px; justify-content: center;
    color: var(--white); font-size: 44px;
  }
  .card--front .wordmark__dot { background: var(--white); width: 24px; height: 24px; }
  .website {
    position: absolute; left: 0; right: 0; top: 302px; text-align: center;
    font-family: "Roboto", sans-serif; font-size: 14px; color: var(--white);
  }

  /* Back */
  .card--back { background: var(--white); }
  .card--back .landmark-area {
    left: 78px; right: auto; top: 196px; width: 62px; height: 134px;
    background: linear-gradient(180deg, rgba(238,138,44,0.05), rgba(238,138,44,0.09));
  }
  .card--back .wordmark {
    position: absolute; left: 18px; top: 152px; width: 200px;
    color: var(--brand-orange); font-size: 19px; gap: 7px; letter-spacing: 0.3px;
  }
  .card--back .wordmark__dot { background: var(--brand-orange); width: 14px; height: 14px; }
  .appointment-title {
    position: absolute; left: 238px; top: 64px;
    font-weight: 800; font-size: 38px; letter-spacing: 0.5px; color: var(--heading-yellow);
  }
  .fields { position: absolute; left: 238px; top: 140px; width: 366px; list-style: none; }
  .field {
    display: flex; align-items: baseline; gap: 10px; height: 40px;
    font-weight: 800; font-size: 14px; color: var(--label-grey);
  }
  .field__line { flex: 1; border-bottom: 1px dotted var(--rule-grey); }
  .field--phone { margin-top: 3px; }
  .footer-band { position: absolute; left: 0; bottom: 0; width: 640px; height: 37px; }
</style>
</head>
<body>
<main class="sheet">
  <section class="card card--front" aria-label="Card front">
    <div class="landmark-area" role="img" aria-label="Faint landmark statue silhouette"></div>
    <div class="wordmark"><span class="wordmark__dot"></span><span>Lumera Solar</span></div>
    <p class="website">www.lumerasolar.com</p>
  </section>

  <section class="card card--back" aria-label="Card back">
    <div class="landmark-area" role="img" aria-label="Faint landmark statue silhouette"></div>
    <div class="wordmark"><span class="wordmark__dot"></span><span>Lumera Solar</span></div>
    <h1 class="appointment-title">APPOINTMENT</h1>
    <ul class="fields">
      <li class="field"><span>DATE:</span><span class="field__line"></span></li>
      <li class="field"><span>TIME:</span><span class="field__line"></span></li>
      <li class="field"><span>REPRESENTATIVE:</span><span class="field__line"></span></li>
      <li class="field field--phone"><span>PHONE :</span><span class="field__line"></span></li>
    </ul>
    <svg class="footer-band" viewBox="0 0 640 37" aria-hidden="true">
      <defs>
        <linearGradient id="bandGrey" x1="0" y1="0" x2="0" y2="1">
          <stop offset="0" stop-color="#8a8a8a"/>
          <stop offset="1" stop-color="#4a4a4a"/>
        </linearGradient>
      </defs>
      <polygon points="0,0 400,0 436,37 0,37" fill="#e37b17"/>
      <polygon points="418,0 640,0 640,37 454,37" fill="url(#bandGrey)"/>
    </svg>
  </section>
</main>
</body>
</html>
```